Visitenkarten-Design für Familienunternehmen (Apotheke)
Zielgruppe
Wir sind ein Familienunternehmen und betreiben 4 Apotheken (alle eigene Namen: Lindenhof-Apotheke; Kessel-Apotheke; Apotheke St. Ottilien und VeroNova-Apotheke)
Wir beginnen, diese alle unter Sperling-Apotheken zusammenzufassen. www.sperling-apotheken.de (die VeroNova-Apotheke eröffnet erst am 1.1.18 neu, daher noch nicht online)
Konkret möchten wir für die Mitarbeiter der VeroNova-Apotheke Visitenkarten mit Porträt für Kunden erstellen.
Aktuell sind wir ca. 10 Mitarbeiter in dieser Apotheke. Ggf. möchten wir mittelfristig alle Mitarbeiter aller Apotheken (ca. 50-60) mit Visitenkarten ausstatten.
Aufgabenstellung
Wir haben vor Jahren selbst laienhaft eine Visitenkarte erstellt
Ich habe gegoogelt und andere Beispiele mit Porträt gefunden.
Wir suchen eine Visitenkarte, die sowohl das Logo VeroNova-Apotheke inkl. Adresse, Telefonnummer etc. hat (kann auch optisch verschoben werden - oben Logo - unten Adresse o.ä) , den Namen des Mitarbeitern und Beruf (Apothekerin o.ä.) und 2-3 Schlagwörter/Schlagsätze zu der Qualifikation des Mitarbeiters.
(die VeroNova-Apotheke hat eine Spezialzertifizierung 'Wiegensichere Offizin' und darf daher auch das Logo Wiegensichere Offizin nutzen. Eventuell gibt es die Möglichkeit dieses auch - nicht konkurrierend - neben dem Hauptlogo VeroNova-Apotheke unterzubringen)
unten gerne 'Sperling-Apotheken' o.ä. als Dachmarke
Mutter-Kind-Expertin (Zertifizierung Wiegensichere Offizin)
Fachberaterin für Darmgesundheit
!! Seriös, weniger verspielt. Druckbar für Druckwerk24, wir nehmen gerne Tipps zu Papier und Stärke an!
Ziel: Klares Design, wo einfach der Kopf des Mitarbeiters gewechselt werden kann und die Qualifikation, um für alle Mitarbeiter gleiche CI zu erstellen

```html
<!DOCTYPE html>
<html lang="de">
<head>
<meta charset="utf-8">
<title>Visitenkarte – VeroNova-Apotheke</title>
<link href="https://fonts.googleapis.com/css2?family=Open+Sans:ital,wght@0,400;0,600;0,700;1,600&display=swap" rel="stylesheet">
<style>
  :root {
    --backdrop: #cfbe91;
    --card: #ffffff;
    --ink: #1a1a1a;
    --contact: #4a4a4a;
    --accent: #e2121b;
    --muted: #a9a9a9;
    --portrait-dark: #2b2320;
    --portrait-light: #6a5446;
  }
  html, body {
    margin: 0;
    padding: 0;
    width: 1015px;
    height: 1200px;
    overflow: hidden;
    background: var(--backdrop);
    font-family: "Open Sans", Arial, sans-serif;
  }
  .business-card {
    position: absolute;
    left: 57px;
    top: 309px;
    width: 900px;
    height: 582px;
    background: var(--card);
    box-shadow: 0 18px 40px rgba(0,0,0,0.18);
    overflow: hidden;
  }
  .brand {
    position: absolute;
    left: 48px;
    top: 54px;
    display: flex;
    align-items: center;
    gap: 12px;
  }
  .brand-name {
    font-size: 30px;
    font-weight: 700;
    color: var(--ink);
    letter-spacing: -0.5px;
    line-height: 1;
  }
  .brand-dot {
    width: 14px;
    height: 14px;
    border-radius: 50%;
    background: var(--accent);
  }
  .contact {
    position: absolute;
    left: 430px;
    top: 52px;
    font-size: 15px;
    line-height: 21px;
    color: var(--contact);
  }
  .contact p { margin: 0; }
  .contact .web-main { color: var(--accent); font-weight: 600; }
  .person {
    position: absolute;
    left: 48px;
    top: 200px;
  }
  .person-name {
    margin: 0;
    font-size: 36px;
    font-weight: 700;
    color: var(--ink);
    line-height: 1.15;
  }
  .person-branch {
    margin: 2px 0 0;
    font-size: 24px;
    font-weight: 600;
    font-style: italic;
    color: var(--accent);
  }
  .person-role {
    margin: 4px 0 0;
    font-size: 22px;
    color: var(--muted);
  }
  .portrait {
    position: absolute;
    left: 520px;
    top: 250px;
    width: 330px;
    height: 332px;
    background: radial-gradient(ellipse at 50% 40%, var(--portrait-light) 0%, var(--portrait-dark) 75%);
  }
  .corner-frame {
    position: absolute;
    right: 0;
    bottom: 0;
  }
</style>
</head>
<body>
  <article class="business-card">
    <div class="brand">
      <span class="brand-name">VeroNova-Apotheke</span>
      <span class="brand-dot"></span>
    </div>

    <div class="contact">
      <p>Gerberweg 12 - 84032 Landshut - Tel.: 0871 / 43 26 510</p>
      <p>Fax: 43 26 511 - veronova@sperling-apotheken.de</p>
      <p class="web-main">www.sperling-apotheken.de</p>
      <p>www.wiegensichere-offizin.de</p>
    </div>

    <div class="person">
      <h1 class="person-name">Lena Hartwig</h1>
      <p class="person-branch">Apotheke St. Ottilien</p>
      <p class="person-role">Apothekerin und andere Qualifikation</p>
    </div>

    <div class="portrait" role="img" aria-label="Porträtfoto der Mitarbeiterin"></div>

    <svg class="corner-frame" width="200" height="170" viewBox="0 0 200 170" aria-hidden="true">
      <polygon points="200,0 200,170 40,170 40,150 180,150 180,0" fill="var(--accent)"/>
    </svg>
  </article>
</body>
</html>
```